Business Consulting Company needs a business card designed

We need a business card in Brisbane Australia for a company called " Marrowvale Consulting Group". I would like to see the designs either in purple or green color

```html
<!DOCTYPE html>
<html lang="en">
<head>
<meta charset="utf-8">
<title>Marrowvale Consulting Group – Business Card</title>
<link href="https://fonts.googleapis.com/css2?family=Exo+2:wght@400;500&display=swap" rel="stylesheet">
<style>
  :root {
    --page: #e9ecef;
    --card: #f7f7f8;
    --card-edge: #e4e5e7;
    --brand: #2e9a5a;
    --brand-light: #4cc27a;
    --brand-deep: #1e7444;
    --ink: #2b2b2e;
    --rule: #7a7d82;
  }
  * { box-sizing: border-box; margin: 0; padding: 0; }
  html, body { width: 1200px; height: 900px; overflow: hidden; }
  body {
    background: var(--page);
    font-family: "Exo 2", sans-serif;
    color: var(--ink);
    display: flex;
    flex-direction: column;
    align-items: center;
    justify-content: center;
    gap: 40px;
  }
  .card {
    position: relative;
    width: 700px;
    height: 400px;
    background: linear-gradient(135deg, #ffffff 0%, var(--card) 55%, var(--card-edge) 100%);
    box-shadow: 0 8px 24px rgba(0,0,0,0.18);
    overflow: hidden;
  }
  .brand {
    display: flex;
    flex-direction: column;
    align-items: center;
    gap: 10px;
    color: var(--brand);
    font-weight: 500;
    letter-spacing: 0.5px;
    text-align: center;
    line-height: 1.05;
  }
  .brand-dot {
    border-radius: 50%;
    background: var(--brand);
    flex: none;
  }
  .brand-name span { display: block; }

  /* back */
  .card-back { display: flex; align-items: center; justify-content: center; }
  .card-back .brand { font-size: 34px; }
  .card-back .brand-dot { width: 66px; height: 66px; }

  /* front */
  .contact {
    position: absolute;
    left: 44px;
    top: 52px;
    font-size: 17px;
    letter-spacing: 1px;
    line-height: 1.35;
  }
  .contact-address { margin-bottom: 16px; }
  .contact-list { list-style: none; }
  .contact-list li {
    display: flex;
    align-items: center;
    gap: 12px;
    height: 33px;
  }
  .contact-list svg { width: 18px; height: 18px; fill: var(--ink); flex: none; }
  .contact-list .email { font-size: 15px; }

  .card-front .brand {
    position: absolute;
    right: 40px;
    top: 96px;
    width: 330px;
    font-size: 27px;
  }
  .card-front .brand-dot { width: 50px; height: 50px; }

  .holder {
    position: absolute;
    right: 44px;
    top: 236px;
    text-align: right;
    text-transform: uppercase;
  }
  .holder-name { font-size: 23px; font-weight: 500; letter-spacing: 2px; }
  .holder-role { font-size: 15px; letter-spacing: 2px; margin-top: 2px; }

  .swoosh { position: absolute; left: 0; bottom: 0; width: 700px; height: 120px; }
</style>
</head>
<body>

<section class="card card-back" aria-label="Card back">
  <div class="brand">
    <span class="brand-dot"></span>
    <p class="brand-name"><span>Marrowvale Consulting</span><span>Group</span></p>
  </div>
</section>

<section class="card card-front" aria-label="Card front">
  <div class="contact">
    <p class="contact-address">Level 18, 83 Ann Street<br>Brisbane QLD</p>
    <ul class="contact-list">
      <li>
        <svg viewBox="0 0 24 24"><path d="M6.6 10.8a15.1 15.1 0 0 0 6.6 6.6l2.2-2.2a1 1 0 0 1 1-.25 11.4 11.4 0 0 0 3.6.57 1 1 0 0 1 1 1V20a1 1 0 0 1-1 1A17 17 0 0 1 3 4a1 1 0 0 1 1-1h3.5a1 1 0 0 1 1 1c0 1.25.2 2.45.57 3.6a1 1 0 0 1-.25 1z"/></svg>
        <span>07 3210 4455</span>
      </li>
      <li>
        <svg viewBox="0 0 24 24"><path d="M7 1h10a2 2 0 0 1 2 2v18a2 2 0 0 1-2 2H7a2 2 0 0 1-2-2V3a2 2 0 0 1 2-2zm0 3v14h10V4zm5 15.2a1.2 1.2 0 1 0 0 2.4 1.2 1.2 0 0 0 0-2.4z"/></svg>
        <span>0412 318 207</span>
      </li>
      <li>
        <svg viewBox="0 0 24 24"><path d="M2 8h3V3h11l3 3v2h3v13H2zm5-3v5h10V7h-3V5zm2 8v2h2v-2zm4 0v2h2v-2zm4 0v2h2v-2zm-8 4v2h2v-2zm4 0v2h2v-2zm4 0v2h2v-2z"/></svg>
        <span>07 3210 4456</span>
      </li>
      <li>
        <svg viewBox="0 0 24 24"><path d="M2 5h20v14H2zm2 2v.5l8 5.5 8-5.5V7zm0 3v7h16v-7l-8 5.5z"/></svg>
        <span class="email">daniel@marrowvale.com</span>
      </li>
    </ul>
  </div>

  <div class="brand">
    <span class="brand-dot"></span>
    <p class="brand-name"><span>Marrowvale Consulting</span><span>Group</span></p>
  </div>

  <div class="holder">
    <p class="holder-name">Daniel Hartley</p>
    <p class="holder-role">Financial Advisor</p>
  </div>

  <svg class="swoosh" viewBox="0 0 700 120" preserveAspectRatio="none" aria-hidden="true">
    <defs>
      <linearGradient id="band" x1="0" y1="0" x2="1" y2="0">
        <stop offset="0" stop-color="var(--brand-deep)"/>
        <stop offset="0.5" stop-color="var(--brand-light)"/>
        <stop offset="1" stop-color="var(--brand)"/>
      </linearGradient>
    </defs>
    <path d="M0 6 C 260 6, 520 36, 700 104" fill="none" stroke="var(--rule)" stroke-width="4"/>
    <path d="M0 20 C 260 20, 500 46, 690 120 L0 120 Z" fill="url(#band)"/>
    <path d="M0 14 C 240 14, 470 36, 640 96" fill="none" stroke="var(--brand)" stroke-width="2"/>
  </svg>
</section>

</body>
</html>
```